Bref créative
Business Cards/Stationary Vandorik Law, P.C.
Professional
Colvin R. Vandorik
Attorney & Counselor at Law
489 Pellham Avenue
Worcester, Massachusetts 01604
Colvin@Vandorik-example.com
www.Vandorik-example.com
I would also like designs to include letterhead and envelopes. Thank you.
Would like to list the areas of practice on the back, Workers' Compensation, Car Accidents, Personal Injury, Family Law, Criminal Law

```html
<!DOCTYPE html>
<html lang="en">
<head>
<meta charset="utf-8">
<title>Vandorik Law, P.C. — Stationery Set</title>
<link href="https://fonts.googleapis.com/css2?family=Cormorant+Garamond:wght@600&family=Open+Sans:wght@400;600&display=swap" rel="stylesheet">
<style>
  :root {
    --stage: #2b2d31;
    --paper: #ffffff;
    --navy: #1f3a7a;
    --navy-deep: #152a5c;
    --grey: #b9bcc2;
    --grey-light: #e6e8ec;
    --ink: #3a3d44;
    --faint: #eef0f4;
  }
  * { margin: 0; padding: 0; box-sizing: border-box; }
  html, body { width: 1200px; height: 310px; overflow: hidden; background: var(--stage); }
  .canvas { position: relative; width: 1200px; height: 310px; font-family: "Open Sans", sans-serif; color: var(--ink); }
  .piece { position: absolute; background: var(--paper); overflow: hidden; }
  .wave { position: absolute; left: 0; bottom: 0; width: 100%; }
  .brand { display: flex; align-items: center; gap: 4px; font-family: "Cormorant Garamond", serif; font-weight: 600; color: var(--navy); white-space: nowrap; }
  .brand-mark { background: var(--navy); flex: none; }
  .small { font-size: 4px; line-height: 1.5; }
  .faint-mark { position: absolute; border-radius: 50%; background: var(--faint); }

  .card-logo { left: 12px; top: 12px; width: 132px; height: 108px; background: var(--navy-deep); }
  .card-logo .brand { position: absolute; left: 14px; top: 40px; color: var(--paper); font-size: 13px; }
  .card-logo .brand-mark { width: 10px; height: 10px; background: var(--paper); }
  .card-logo .tagline { position: absolute; left: 28px; top: 60px; font-size: 4px; color: var(--grey); }

  .card-front { left: 12px; top: 212px; width: 120px; height: 62px; }
  .card-front .brand { position: absolute; left: 6px; top: 7px; font-size: 7px; }
  .card-front .brand-mark { width: 6px; height: 6px; }
  .card-front .details { position: absolute; left: 6px; top: 20px; }
  .card-back { left: 139px; top: 212px; width: 120px; height: 62px; background: var(--navy); color: var(--paper); }
  .card-back ul { list-style: none; position: absolute; left: 10px; top: 12px; font-size: 4.5px; line-height: 1.6; }

  .letterhead { top: 18px; width: 200px; height: 270px; }
  .letterhead .brand { position: absolute; left: 12px; top: 12px; font-size: 8px; }
  .letterhead .brand-mark { width: 8px; height: 8px; }
  .letterhead .contact { position: absolute; right: 12px; top: 12px; text-align: right; }
  .letterhead .faint-mark { left: 50px; top: 70px; width: 100px; height: 100px; }
  .letterhead .footer { position: absolute; bottom: 5px; width: 100%; text-align: center; color: var(--paper); font-size: 3.5px; }
  .lh-one { left: 271px; }
  .lh-two { left: 487px; }

  .envelope { width: 228px; height: 104px; }
  .envelope .brand { position: absolute; left: 10px; top: 10px; font-size: 8px; }
  .envelope .brand-mark { width: 8px; height: 8px; }
  .envelope .return { position: absolute; left: 24px; top: 22px; }
  .env-one { left: 696px; top: 52px; }
  .env-two { left: 696px; top: 174px; }

  .env-back { left: 936px; width: 252px; }
  .env-grey { top: 52px; height: 70px; background: var(--grey-light); }
  .env-blue { top: 118px; height: 76px; }
  .env-plain { top: 200px; height: 80px; }
  .env-back .brand { position: absolute; left: 50%; transform: translateX(-50%); font-size: 8px; }
  .env-back .brand-mark { width: 8px; height: 8px; }
</style>
</head>
<body>
<main class="canvas">

  <section class="piece card-logo" aria-label="Business card, logo side">
    <div class="brand"><span class="brand-mark"></span>Vandorik Law, P.C.</div>
    <p class="tagline">Attorney &amp; Counselor at Law</p>
  </section>

  <section class="piece card-front" aria-label="Business card, contact side">
    <div class="brand"><span class="brand-mark"></span>Vandorik Law, P.C.</div>
    <div class="details small">
      <strong>Colvin R. Vandorik</strong><br>
      Attorney &amp; Counselor at Law<br>
      489 Pellham Avenue, Worcester, MA 01604<br>
      Tel (508) 555-0142 · Colvin@Vandorik-example.com
    </div>
    <svg class="wave" viewBox="0 0 120 14" height="14" preserveAspectRatio="none">
      <path d="M0 6 C40 14 80 0 120 4 V14 H0 Z" fill="var(--grey)"/>
      <path d="M0 9 C40 16 80 3 120 7 V14 H0 Z" fill="var(--navy)"/>
    </svg>
  </section>

  <section class="piece card-back" aria-label="Business card, practice areas">
    <ul>
      <li>Workers' Compensation</li>
      <li>Car Accidents</li>
      <li>Personal Injury</li>
      <li>Family Law</li>
      <li>Criminal Law</li>
    </ul>
  </section>

  <section class="piece letterhead lh-one" aria-label="Letterhead">
    <div class="brand"><span class="brand-mark"></span>Vandorik Law, P.C.</div>
    <div class="contact small">489 Pellham Avenue<br>Worcester, MA 01604<br>(508) 555-0142</div>
    <span class="faint-mark"></span>
    <svg class="wave" viewBox="0 0 200 26" height="26" preserveAspectRatio="none">
      <path d="M0 8 C70 22 130 0 200 6 V26 H0 Z" fill="var(--grey)"/>
      <path d="M0 12 C70 26 130 4 200 10 V26 H0 Z" fill="var(--navy)"/>
    </svg>
    <p class="footer">www.Vandorik-example.com</p>
  </section>

  <section class="piece letterhead lh-two" aria-label="Letterhead, second page">
    <div class="brand"><span class="brand-mark"></span>Vandorik Law, P.C.</div>
    <div class="contact small">Colvin@Vandorik-example.com<br>www.Vandorik-example.com<br>Fax (508) 555-0143</div>
    <span class="faint-mark"></span>
    <svg class="wave" viewBox="0 0 200 26" height="26" preserveAspectRatio="none">
      <path d="M0 8 C70 22 130 0 200 6 V26 H0 Z" fill="var(--grey)"/>
      <path d="M0 12 C70 26 130 4 200 10 V26 H0 Z" fill="var(--navy)"/>
    </svg>
    <p class="footer">489 Pellham Avenue · Worcester, Massachusetts 01604</p>
  </section>

  <section class="piece envelope env-one" aria-label="Envelope front">
    <div class="brand"><span class="brand-mark"></span>Vandorik Law, P.C.</div>
    <div class="return small">489 Pellham Avenue<br>Worcester, MA 01604</div>
    <svg class="wave" viewBox="0 0 228 18" height="18" preserveAspectRatio="none">
      <path d="M0 6 C80 18 150 0 228 4 V18 H0 Z" fill="var(--grey)"/>
      <path d="M0 9 C80 20 150 3 228 8 V18 H0 Z" fill="var(--navy)"/>
    </svg>
  </section>

  <section class="piece envelope env-two" aria-label="Envelope front, alternate">
    <div class="brand"><span class="brand-mark"></span>Vandorik Law, P.C.</div>
    <div class="return small">489 Pellham Avenue<br>Worcester, MA 01604</div>
    <svg class="wave" viewBox="0 0 228 18" height="18" preserveAspectRatio="none">
      <path d="M0 6 C80 18 150 0 228 4 V18 H0 Z" fill="var(--grey)"/>
      <path d="M0 9 C80 20 150 3 228 8 V18 H0 Z" fill="var(--navy)"/>
    </svg>
  </section>

  <section class="piece env-back env-grey" aria-label="Envelope back, grey flap">
    <svg width="252" height="70" viewBox="0 0 252 70">
      <path d="M0 0 L126 40 L252 0 V0 Z" fill="#8f939b"/>
    </svg>
  </section>

  <section class="piece env-back env-blue" aria-label="Envelope back, blue flap">
    <svg width="252" height="76" viewBox="0 0 252 76" style="position:absolute;left:0;top:0">
      <path d="M0 0 H252 L126 44 Z" fill="var(--navy)"/>
      <path d="M0 0 L126 44 L252 0" fill="none" stroke="var(--grey)" stroke-width="1.5"/>
    </svg>
    <div class="brand" style="top:50px"><span class="brand-mark"></span>Vandorik Law, P.C.</div>
  </section>

  <section class="piece env-back env-plain" aria-label="Envelope back, white flap">
    <svg width="252" height="80" viewBox="0 0 252 80" style="position:absolute;left:0;top:0">
      <path d="M0 0 L126 40 L252 0" fill="none" stroke="var(--grey)" stroke-width="1"/>
    </svg>
    <div class="brand" style="top:14px"><span class="brand-mark"></span>Vandorik Law, P.C.</div>
  </section>

</main>
</body>
</html>
```